TRL Cards
Business Cards - Financial Services
Business Cards
Professional
Dominic Hale
Managing Director of Digital Services
387 Marlowe St Suite 204 New York, NY 10017
dhale@trlwealthco.example
www.trlwealthco.example
sarmadshaikh sarmadshaikh
sir its not getting aplosd
ruxanda ruxanda
Please uploud your logo in .ai format

```html
<!DOCTYPE html>
<html lang="en">
<head>
<meta charset="utf-8">
<title>TRL Cards – Business Card</title>
<link href="https://fonts.googleapis.com/css2?family=Open+Sans:wght@400;600&display=swap" rel="stylesheet">
<style>
  :root{
    --bg:#d9d9d9;
    --card:#ffffff;
    --green:#1f5a2e;
    --green-dark:#123d1e;
    --gold:#a8915a;
    --ink:#3a3a3a;
    --title:#8a7a4e;
  }
  *{margin:0;padding:0;box-sizing:border-box}
  html,body{width:1200px;height:878px;overflow:hidden}
  body{background:var(--bg);font-family:"Open Sans",Arial,sans-serif;position:relative}
  .card{position:absolute;width:520px;height:297px;background:var(--card);overflow:hidden;box-shadow:0 6px 18px rgba(0,0,0,.18)}
  .card--front{left:50px;top:290px}
  .card--back{left:630px;top:290px}

  .brand{display:flex;align-items:center;gap:10px}
  .brand__dot{width:34px;height:34px;border-radius:50%;background:var(--green)}
  .brand__name{font-weight:600;color:var(--green);letter-spacing:1px}

  .card--front .brand{position:absolute;left:34px;top:28px}
  .card--front .brand__name{font-size:30px}

  .contact{position:absolute;left:36px;top:104px;list-style:none;font-size:13px;color:var(--ink);line-height:19px}
  .contact li{display:flex;align-items:center;gap:8px}
  .contact svg{width:11px;height:11px;fill:var(--ink)}

  .person{position:absolute;right:38px;top:122px;text-align:right}
  .person__name{font-size:17px;font-weight:600;color:var(--green)}
  .person__title{font-size:12px;color:var(--title);margin-top:2px}

  .address{position:absolute;right:38px;top:196px;text-align:right;font-size:12.5px;color:var(--ink);line-height:17px;max-width:230px}

  .swoosh{position:absolute;left:0;bottom:0;width:520px;height:297px}

  .card--back .brand{position:absolute;left:50%;top:50%;transform:translate(-50%,-50%)}
  .card--back .brand__dot{width:56px;height:56px}
  .card--back .brand__name{font-size:48px}
</style>
</head>
<body>
  <section class="card card--front">
    <svg class="swoosh" viewBox="0 0 520 297" aria-hidden="true">
      <path d="M0 170 C 80 225, 230 262, 520 272 L520 297 L0 297 Z" fill="var(--gold)"/>
      <path d="M0 178 C 80 232, 230 268, 520 277 L520 297 L0 297 Z" fill="var(--card)"/>
      <path d="M0 186 C 90 245, 260 282, 520 290 L520 297 L0 297 Z" fill="var(--green)"/>
    </svg>

    <div class="brand">
      <span class="brand__dot"></span>
      <span class="brand__name">TRL</span>
    </div>

    <ul class="contact">
      <li><svg viewBox="0 0 24 24"><path d="M6.6 10.8a15.1 15.1 0 0 0 6.6 6.6l2.2-2.2a1 1 0 0 1 1-.25 11.4 11.4 0 0 0 3.6.57 1 1 0 0 1 1 1V20a1 1 0 0 1-1 1A17 17 0 0 1 3 4a1 1 0 0 1 1-1h3.5a1 1 0 0 1 1 1c0 1.25.2 2.45.57 3.6a1 1 0 0 1-.25 1z"/></svg>212 555 0147</li>
      <li><svg viewBox="0 0 24 24"><path d="M6 2h12v6H6z M4 9h16a2 2 0 0 1 2 2v6h-4v5H6v-5H2v-6a2 2 0 0 1 2-2zm4 8v3h8v-3z"/></svg>212 555 0148</li>
      <li><svg viewBox="0 0 24 24"><path d="M2 5h20v14H2z M3 6l9 7 9-7" stroke="#fff" stroke-width="1.5"/></svg>dhale@trlwealthco.example</li>
    </ul>

    <div class="person">
      <p class="person__name">Dominic Hale</p>
      <p class="person__title">Managing Director</p>
    </div>

    <p class="address">387 Marlowe St Suite 204<br>New York, NY 10017</p>
  </section>

  <section class="card card--back">
    <div class="brand">
      <span class="brand__dot"></span>
      <span class="brand__name">TRL</span>
    </div>
  </section>
</body>
</html>
```